"Tales of Quiet Harbors" Book Cover Design

I am seeking a dynamic, modern, and professional cover design for a book focused on groundbreaking science that explores how a supplement called plasmalogens can revitalize the brain, prevent Alzheimer’s, and safeguard memories. The design should strike a balance between being visually appealing and conveying the seriousness of the topic.

Target Market(s)

The target audience includes individuals who are curious about cutting-edge science and proactive approaches to brain health, as well as those seeking to better understand how to protect their cognitive functions and memories. The cover should resonate with readers interested in health, science, and self-improvement, while reflecting the book’s informative and empowering tone.

Requirements
Must have
• The quotation across the top of the page (this is a placeholder for now, it will be changed eventually) and the author's name.
Should not have
• You don't need to use the puzzle idea!

```html
<!DOCTYPE html>
<html lang="en">
<head>
<meta charset="utf-8">
<title>Tales of Quiet Harbors – Cover Wrap</title>
<link rel="stylesheet" href="https://fonts.googleapis.com/css2?family=Bebas+Neue&family=Josefin+Sans:wght@400;700&family=Poppins:wght@400;600&display=swap">
<style>
  :root {
    --page-bg: #3f5260;
    --paper: #ffffff;
    --navy: #1b3557;
    --blue: #1f6aaa;
    --sky: #6fb4e4;
    --deep: #0f5b9c;
    --ink: #1e1e1e;
  }
  * { margin: 0; padding: 0; box-sizing: border-box; }
  html, body { width: 792px; height: 1200px; overflow: hidden; }
  body { background: var(--page-bg); position: relative; }

  .wrap {
    position: absolute;
    left: 16px; top: 336px;
    width: 1240px; height: 860px;
    background: var(--paper);
    transform: scale(0.6129);
    transform-origin: 0 0;
    overflow: hidden;
    box-shadow: 0 10px 30px rgba(0,0,0,0.35);
  }
  .wrap > * { position: absolute; }

  /* Back cover */
  .back-title {
    left: 42px; top: 52px;
    font-family: "Bebas Neue", sans-serif;
    font-size: 68px; line-height: 62px;
    color: var(--navy);
  }
  .back-title .accent { color: var(--blue); }
  .blurb {
    left: 42px; top: 198px; width: 500px;
    font-family: "Poppins", sans-serif;
    font-size: 12.3px; line-height: 14.4px;
    color: var(--ink);
  }
  .about-label {
    left: 40px; top: 464px;
    font-family: "Poppins", sans-serif;
    font-size: 23px; color: var(--sky);
  }
  .about-name {
    left: 40px; top: 494px;
    font-family: "Josefin Sans", sans-serif;
    font-weight: 700; font-size: 22px;
    color: var(--ink);
  }
  .about-name .cred { font-weight: 400; }
  .author-photo {
    left: 42px; top: 534px; width: 105px; height: 104px;
    background: linear-gradient(160deg, #b9c8d6, #6d7f90);
  }
  .bio {
    left: 163px; top: 540px; width: 390px;
    font-family: "Poppins", sans-serif;
    font-size: 12.3px; line-height: 14.4px;
    color: var(--ink);
  }

  /* Spine */
  .spine-title, .spine-author {
    font-family: "Josefin Sans", sans-serif;
    font-weight: 700;
    writing-mode: vertical-rl;
    white-space: nowrap;
  }
  .spine-title { left: 604px; top: 40px; font-size: 29px; color: var(--navy); }
  .spine-title .accent { color: var(--blue); }
  .spine-author { left: 612px; top: 624px; font-size: 17px; color: var(--ink); }
  .spine-author .cred { font-weight: 400; }

  /* Front cover */
  .quote-mark {
    left: 700px; top: 18px;
    font-family: "Poppins", sans-serif; font-weight: 600;
    font-size: 90px; line-height: 90px; color: var(--blue);
  }
  .quote {
    left: 700px; top: 86px; width: 380px;
    font-family: "Poppins", sans-serif;
    font-size: 20.5px; line-height: 24px; color: var(--ink);
  }
  .quote-source {
    left: 700px; top: 142px;
    font-family: "Poppins", sans-serif; font-weight: 600;
    font-size: 19px; color: var(--blue);
  }
  .cover-art {
    left: 695px; top: 200px; width: 545px; height: 660px;
    border-radius: 260px 0 0 0;
    background: linear-gradient(90deg, var(--sky) 0%, #4c97d1 40%, var(--deep) 75%, #0b4f8c 100%);
  }
  .front-title {
    left: 787px; top: 318px;
    font-family: "Bebas Neue", sans-serif;
    font-size: 106px; line-height: 90px;
    color: var(--navy);
  }
  .front-title .light { color: var(--paper); }
  .front-author {
    left: 700px; top: 768px;
    font-family: "Josefin Sans", sans-serif; font-weight: 700;
    font-size: 22px; line-height: 27px; color: var(--ink);
  }
  .front-author .cred { font-weight: 400; }
</style>
</head>
<body>
  <div class="wrap">
    <!-- Back cover -->
    <h2 class="back-title">Tales of<br><span class="accent">Quiet Harbors</span></h2>
    <p class="blurb">Lorem ipsum dolor sit amet, consectetur adipiscing elit, sed do eiusmod tempor incididunt ut labore et dolore magna aliqua. Quis ipsum suspendisse ultrices gravida. Risus commodo viverra maecenas accumsan lacus vel facilisis. Lorem ipsum dolor sit amet, consectetur adipiscing elit, sed do eiusmod tempor incididunt ut labore et dolore magna aliqua. Quis ipsum suspendisse ultrices gravida. Risus commodo viverra maecenas accumsan lacus vel facilisis. Lorem ipsum dolor sit amet, consectetur adipiscing elit, sed do eiusmod tempor incididunt ut labore et dolore magna aliqua. Quis ipsum suspendisse ultrices gravida. Risus commodo viverra maecenas accumsan lacus vel facilisis. Lorem ipsum dolor sit amet, consectetur adipiscing elit, sed do eiusmod tempor incididunt ut labore et dolore magna aliqua. Quis ipsum suspendisse ultrices gravida. Risus commodo viverra maecenas accumsan lacus vel facilisis. Lorem ipsum dolor sit amet, consectetur adipiscing elit, sed do eiusmod tempor incididunt ut labore et dolore magna aliqua. Quis ipsum suspendisse ultrices gravida. Risus commodo viverra maecenas accumsan lacus vel facilisis.</p>
    <p class="about-label">About</p>
    <p class="about-name">DANIEL HARTWELL, <span class="cred">MD</span></p>
    <div class="author-photo" role="img" aria-label="Portrait photograph of the author"></div>
    <p class="bio">Lorem ipsum dolor sit amet, consectetur adipiscing elit, sed do eiusmod tempor incididunt ut labore et dolore magna aliqua. Quis ipsum suspendisse ultrices gravida. Risus commodo viverra maecenas accumsan lacus vel facilisis. Lorem ipsum dolor sit amet, consectetur adipiscing elit, sed do eiusmod tempor incididunt ut labore et dolore magna aliqua. Quis ipsum suspendisse ultrices gravida.</p>

    <!-- Spine -->
    <p class="spine-title">TALES OF <span class="accent">QUIET HARBORS</span></p>
    <p class="spine-author">DANIEL HARTWELL, <span class="cred">MD</span></p>

    <!-- Front cover -->
    <p class="quote-mark">&ldquo;</p>
    <p class="quote">An incredible guide to protecting your mind and memories.</p>
    <p class="quote-source">- Dr Anil Mehra, MD</p>
    <div class="cover-art" role="img" aria-label="Illustration of a head in profile breaking apart into blue shards"></div>
    <h1 class="front-title">Tales<br>of<br><span class="light">Quiet</span><br><span class="light">Harbors</span></h1>
    <p class="front-author">DANIEL<br>HARTWELL, <span class="cred">MD</span></p>
  </div>
</body>
</html>
```